I need a great, modern, professional website for my paint contracting company, Ashbrook Coating Contractors, LLC. I have many good pix that can be used from jobs completed that would be attractive. We do commercial, residential and industrial jobs. I’m fully insured and licensed, including holding a General Contractor’s License as a Subcontractor. I know nothing about coding websites. I’ll have my assistant get on tomorrow and learn how to drop files. I’m not sure what files to send. This will be difficult at best, it being able to talk this through. Oh well. What’s next?

Target Market(s)

General Contractors

Industry/Entity Type

Paint Contracting

Coding

Coded - Design and coding required

Font styles to use
Sans Serif

Colors
00AB8E
00BBA5
67D7C9
C6EFE9
E9F9F6

Requirements
Must have
• Pix of completed jobs, bio, maybe testimonials from happy customers? ….
Nice to have
• I’d like it to have a modern appeal, but still have some warmth.
Should not have
• ??

```html
<!DOCTYPE html>
<html lang="en">
<head>
<meta charset="utf-8">
<title>Ashbrook Coating Contractors, LLC</title>
<link rel="stylesheet" href="https://fonts.googleapis.com/css2?family=Poppins:wght@400;500;600;700;800&display=swap">
<style>
:root{
  --teal:#00AB8E;
  --teal-2:#00BBA5;
  --teal-3:#67D7C9;
  --teal-4:#C6EFE9;
  --teal-5:#E9F9F6;
  --ink:#3d3d4e;
  --body:#6b6b78;
  --grey-bg:#f4f4f4;
  --footer:#4a4a5f;
  --purple:#ad8bf2;
  --yellow:#fed06e;
  --green:#a7d874;
  --white:#ffffff;
}
*{box-sizing:border-box;margin:0;padding:0}
html,body{width:1200px;height:4410px;overflow:hidden}
body{font-family:"Poppins",sans-serif;color:var(--ink);background:var(--white);position:relative}
.photo{position:absolute}

/* header */
.site-header{position:absolute;left:0;top:0;width:1200px;height:68px;background:var(--white)}
.brand{position:absolute;left:88px;top:20px;display:flex;align-items:center;gap:8px;font-weight:700;font-size:21px;color:var(--ink)}
.brand-mark{width:26px;height:26px;border:2px solid var(--teal);display:block}
.main-nav{position:absolute;left:500px;top:0;height:68px;display:flex;gap:25px;align-items:center}
.main-nav a{font-size:11px;font-weight:500;color:var(--ink);text-decoration:none;text-transform:uppercase;height:68px;line-height:68px;position:relative}
.main-nav a.active{color:var(--teal)}
.main-nav a.active::before{content:"";position:absolute;left:0;right:0;top:0;height:3px;background:var(--teal)}
.call-box{position:absolute;left:1015px;top:0;width:185px;height:68px;background:var(--teal-2);color:var(--white)}
.call-icon{position:absolute;left:0;top:0;width:58px;height:68px;background:var(--teal);display:flex;align-items:center;justify-content:center}
.call-text{position:absolute;left:75px;top:18px;font-size:10px;font-weight:600;line-height:1.2}
.call-text strong{display:block;font-size:14px;font-weight:700}

/* hero */
.hero-photo{left:0;top:68px;width:1200px;height:647px;background:linear-gradient(100deg,#5fb3d2 0%,#7cc3dc 40%,#c9e4ee 60%,#e8e8ea 100%)}
.hero-title{position:absolute;left:88px;top:225px;font-size:62px;font-weight:800;line-height:66px;color:var(--white)}
.hero-sub{position:absolute;left:88px;top:438px;font-size:23px;font-weight:500;color:var(--white)}
.btn-outline{position:absolute;left:88px;top:493px;width:178px;height:46px;background:var(--white);font-size:12px;font-weight:700;color:var(--ink);display:flex;align-items:center;justify-content:center;text-transform:uppercase}
.btn-outline::after{content:"";position:absolute;left:6px;top:6px;right:-6px;bottom:-6px;border:2px solid var(--white)}

/* services */
.service{position:absolute;top:715px;width:400px;height:222px;color:var(--white)}
.service h3{position:absolute;left:103px;top:62px;font-size:22px;font-weight:700}
.service p{position:absolute;left:103px;top:100px;width:260px;font-size:12.5px;line-height:20px}
.service-art{position:absolute;left:0;top:50px;width:75px;height:110px;background:rgba(255,255,255,.14)}
.svc-industry{left:0;background:var(--purple)}
.svc-residential{left:400px;background:var(--yellow)}
.svc-commercial{left:800px;background:var(--green)}

/* about */
.about{position:absolute;left:0;top:937px;width:1200px;height:616px;background:var(--grey-bg)}
.about-photo{left:0;top:0;width:520px;height:616px;background:linear-gradient(90deg,#dfe6ea,#ece7dc 60%,var(--grey-bg))}
.eyebrow{font-size:15px;font-weight:500;color:#8a8a95}
.about .eyebrow{position:absolute;left:625px;top:130px}
.about h2{position:absolute;left:625px;top:155px;font-size:35px;font-weight:700;line-height:41px;color:var(--ink)}
.about-rule{position:absolute;left:597px;top:247px;width:68px;height:2px;background:#b5b5bb}
.about p{position:absolute;left:625px;top:263px;width:455px;font-size:13.5px;line-height:22px;color:var(--body)}
.btn-solid{position:absolute;background:var(--teal-2);color:var(--white);font-size:12px;font-weight:700;text-transform:uppercase;display:flex;align-items:center;justify-content:center}
.about .btn-solid{left:626px;top:465px;width:152px;height:46px}

/* inspiration */
.section-title{position:absolute;left:0;width:1200px;text-align:center;font-size:35px;font-weight:600;color:var(--ink)}
.inspo-1{left:189px;top:1702px;width:480px;height:265px;background:linear-gradient(90deg,#e9ecee,#dfe4e8 50%,#a9cdea)}
.inspo-2{left:677px;top:1702px;width:334px;height:265px;background:linear-gradient(90deg,#f3d44a,#e8d36b 60%,#ebebe8)}
.inspo-3{left:189px;top:1975px;width:270px;height:265px;background:linear-gradient(90deg,#9cc9cc,#b7d6d6)}
.inspo-feature{position:absolute;left:466px;top:1975px;width:269px;height:265px;background:var(--teal-2);color:var(--white)}
.inspo-feature .eyebrow{position:absolute;left:36px;top:64px;color:var(--white);font-size:14px}
.inspo-feature .rule{position:absolute;left:36px;top:96px;width:36px;height:2px;background:var(--white)}
.inspo-feature h3{position:absolute;left:36px;top:118px;font-size:16.5px;font-weight:700;line-height:27px}
.inspo-5{left:741px;top:1975px;width:270px;height:265px;background:linear-gradient(90deg,#e6e9ea,#d7e4c7 60%,#9fc97d)}

/* testimonials */
.testimonial-photo{left:0;top:2347px;width:1200px;height:567px;background:linear-gradient(90deg,#e3eef5,#d6e6f3 30%,#eceeee 55%,#e4e4e2)}
.testimonials h2{position:absolute;left:88px;top:2430px;font-size:35px;font-weight:700;color:var(--ink)}
.quote-card{position:absolute;left:88px;top:2498px;width:414px;height:308px;background:var(--white);border-bottom:2px solid var(--teal)}
.quote-mark{position:absolute;left:47px;top:0}
.quote-card p{position:absolute;left:47px;top:68px;width:325px;font-size:13px;line-height:22px;color:var(--body)}
.quote-author{position:absolute;left:47px;top:252px;display:flex;align-items:center;gap:12px;font-size:12px;font-weight:600;color:var(--ink)}
.quote-author::before{content:"";width:38px;height:2px;background:var(--teal)}

/* news */
.news-card{position:absolute;top:3058px;width:295px;height:368px;background:var(--white);box-shadow:0 6px 20px rgba(0,0,0,.06)}
.news-card .photo{left:0;top:0;width:295px;height:234px}
.news-date{position:absolute;left:29px;top:260px;font-size:11px;color:#8a8a95}
.news-card h3{position:absolute;left:29px;top:283px;font-size:14.5px;font-weight:600;color:var(--ink)}
.news-card p{position:absolute;left:29px;top:310px;width:240px;font-size:12.5px;line-height:18px;color:var(--body)}
.n1{left:145px}.n1 .photo{background:linear-gradient(90deg,#6a9fd6,#dfe3e5 50%,#c9ccc9)}
.n2{left:452px}.n2 .photo{background:linear-gradient(90deg,#d8c9a0,#e7c7a8 50%,#f0c7cf)}
.n3{left:760px}.n3 .photo{background:linear-gradient(90deg,#aedc9e,#c6e3ad 50%,#d6dde4)}

/* quote form */
.quote-intro{position:absolute;left:221px;top:3597px;width:320px}
.quote-intro h2{font-size:35px;font-weight:700;line-height:41px;color:var(--ink)}
.quote-intro p{margin-top:18px;font-size:13px;line-height:22px;color:var(--body)}
.site-footer{position:absolute;left:0;top:3915px;width:1200px;height:495px;background:var(--footer);color:var(--white)}
.quote-form{position:absolute;left:573px;top:3515px;width:407px;height:455px;background:var(--teal-2)}
.field{position:absolute}
.field label{display:block;font-size:10.5px;font-weight:600;color:var(--white);margin-bottom:4px}
.field span{display:block;height:34px;background:rgba(255,255,255,.22)}
.f-name{left:38px;top:36px;width:161px}
.f-email{left:207px;top:36px;width:161px}
.f-phone{left:38px;top:101px;width:161px}
.f-address{left:207px;top:101px;width:161px}
.f-city{left:38px;top:169px;width:161px}
.f-state{left:207px;top:169px;width:161px}
.f-message{left:38px;top:238px;width:330px}
.f-message span{height:92px}
.btn-submit{position:absolute;left:138px;top:397px;width:131px;height:38px;background:var(--white);color:var(--ink);font-size:12px;font-weight:700;display:flex;align-items:center;justify-content:center;text-transform:uppercase}

/* footer */
.foot-col{position:absolute;top:163px}
.foot-col h4{font-size:18px;font-weight:700;margin-bottom:22px}
.foot-links a{display:block;font-size:12px;color:var(--white);text-decoration:none;line-height:26.5px}
.contact-item{display:flex;gap:9px;font-size:12px;line-height:17px;margin-bottom:18px}
.contact-item svg{flex:none;margin-top:3px}
.foot-news p{font-size:12px;line-height:18px;width:250px}
.subscribe{margin-top:18px;width:248px;height:46px;background:var(--white);display:flex;align-items:center;padding:0 16px;gap:8px;font-size:12px;color:#8a8a95}
.subscribe .send{margin-left:auto}
.socials{display:flex;gap:11px}
.socials span{width:40px;height:40px;border-radius:50%;border:1px solid rgba(255,255,255,.3);display:flex;align-items:center;justify-content:center}
.socials span::after{content:"";width:12px;height:12px;border-radius:50%;background:var(--white)}
.foot-rule{position:absolute;left:88px;top:445px;width:1024px;height:1px;background:rgba(255,255,255,.2)}
.copyright{position:absolute;left:0;top:463px;width:1200px;text-align:center;font-size:11.5px;font-weight:600}
.to-top{position:absolute;left:1131px;top:420px;width:44px;height:44px;border-radius:50%;background:var(--teal-2);display:flex;align-items:center;justify-content:center}
</style>
</head>
<body>

<header class="site-header">
  <div class="brand"><span class="brand-mark"></span>Ashbrook Coating</div>
  <nav class="main-nav">
    <a class="active" href="#">Home</a><a href="#">Residential</a><a href="#">Commercial</a><a href="#">Portfolio</a><a href="#">About</a><a href="#">Contact</a>
  </nav>
  <div class="call-box">
    <div class="call-icon"><svg width="16" height="16" viewBox="0 0 24 24"><path fill="#fff" d="M6.6 10.8a15.1 15.1 0 0 0 6.6 6.6l2.2-2.2a1 1 0 0 1 1-.25 11.4 11.4 0 0 0 3.6.57 1 1 0 0 1 1 1V20a1 1 0 0 1-1 1A17 17 0 0 1 3 4a1 1 0 0 1 1-1h3.5a1 1 0 0 1 1 1c0 1.25.2 2.45.57 3.57a1 1 0 0 1-.25 1z"/></svg></div>
    <div class="call-text">CALL US:<strong>123-456-789</strong></div>
  </div>
</header>

<section class="hero">
  <div class="photo hero-photo" role="img" aria-label="Painter on a ladder holding a colour fan deck against a blue painted wall"></div>
  <h1 class="hero-title">All The Best<br>Painting Tools<br>You Need.</h1>
  <p class="hero-sub">Painting Housse Is Our Passion</p>
  <a class="btn-outline">Get A Quote Now</a>
</section>

<section class="services">
  <div class="service svc-industry">
    <div class="service-art" role="img" aria-label="Faint factory line drawing"></div>
    <h3>Industry</h3>
    <p>Aenean sollicitudin bibendum auctor, nisi elit consequat ipsum, nec sagittis sem nibh id elit duis sed odio</p>
  </div>
  <div class="service svc-residential">
    <div class="service-art" role="img" aria-label="Faint house line drawing"></div>
    <h3>Residential</h3>
    <p>Aenean sollicitudin bibendum auctor, nisi elit consequat ipsum, nec sagittis sem nibh id elit duis sed odio</p>
  </div>
  <div class="service svc-commercial">
    <div class="service-art" role="img" aria-label="Faint office building line drawing"></div>
    <h3>Commercial</h3>
    <p>Aenean sollicitudin bibendum auctor, nisi elit consequat ipsum, nec sagittis sem nibh id elit duis sed odio</p>
  </div>
</section>

<section class="about">
  <div class="photo about-photo" role="img" aria-label="Painter in white overalls leaning on a wooden step ladder with a paint bucket"></div>
  <span class="eyebrow">Introduction</span>
  <h2>About Ashbrook Coating<br>Contractors, LLC</h2>
  <span class="about-rule"></span>
  <p>Aenean sollicitudin, lorem quis bibendum auctor, nisi elit consequat ipsum, nec sagittis sem nibh id elit. Duis sed odio sit amet nibh vulputate cursus a sit amet mauris. Morbi accumsan ipsum velit. Nam nec tellus a odio tincidunt auctor a odio. Sed non mauris vitae erat consequat auctor eu in elit. Class aptent taciti sociosqu ad litora torquent per conubia nostra, per inceptos himenaeos. Mauris in erat justo. Nullam ac urna eu felis dapibus condimentum sit amet a augue...</p>
  <a class="btn-solid">Find Out More</a>
</section>

<section class="inspiration">
  <h2 class="section-title" style="top:1627px">Need Some Inspiration?</h2>
  <div class="photo inspo-1" role="img" aria-label="Painter rolling light blue paint onto a white wall"></div>
  <div class="photo inspo-2" role="img" aria-label="Worker in a hard hat rolling yellow paint onto a wall"></div>
  <div class="photo inspo-3" role="img" aria-label="Painter rolling teal paint on a wall"></div>
  <div class="inspo-feature">
    <span class="eyebrow">Painting Colors</span>
    <span class="rule"></span>
    <h3>Mistakes are money.<br>Find the right product<br>with our selector.</h3>
  </div>
  <div class="photo inspo-5" role="img" aria-label="Painter holding a roller with green paint"></div>
</section>

<section class="testimonials">
  <div class="photo testimonial-photo" role="img" aria-label="Painter with a paint roller beside a white wall and a wooden ladder"></div>
  <h2>Testimonials</h2>
  <div class="quote-card">
    <svg class="quote-mark" width="38" height="34" viewBox="0 0 38 34"><path d="M0 0h14v26l-7 8H0z M22 0h14v26l-7 8h-7z" fill="var(--teal)"/></svg>
    <p>Aenean sollicitudin, lorem quis bibendum auctor, nisi elit consequat ipsum, nec sagittis sem nibh id elit. Duis sed odio sit amet nibh vulputate cursus a sit amet mauris. Morbi accumsan ipsum velit. Nam nec tellus a odio tincidunt auctor a odio. Sed non mauris vitae erat consequat auctor eu...</p>
    <div class="quote-author">Marla Jensen | Brightline Homes</div>
  </div>
</section>

<section class="news">
  <h2 class="section-title" style="top:2993px">Latest News</h2>
  <article class="news-card n1">
    <div class="photo" role="img" aria-label="Painter rolling white paint on a wall"></div>
    <span class="news-date">25-05-2022</span>
    <h3>Some heading goes here</h3>
    <p>Aenean sollicitudin lorem quis nisi elit consequat ipsum nec...</p>
  </article>
  <article class="news-card n2">
    <div class="photo" role="img" aria-label="Two workers in hard hats painting a pink wall"></div>
    <span class="news-date">25-05-2022</span>
    <h3>Some heading goes here</h3>
    <p>Aenean sollicitudin lorem quis nisi elit consequat ipsum nec...</p>
  </article>
  <article class="news-card n3">
    <div class="photo" role="img" aria-label="Couple painting a room green from a step ladder"></div>
    <span class="news-date">25-05-2022</span>
    <h3>Some heading goes here</h3>
    <p>Aenean sollicitudin lorem quis nisi elit consequat ipsum nec...</p>
  </article>
</section>

<section class="quote-intro">
  <h2>Start With A Free<br>Quote!</h2>
  <p>We are one of the best paint contracting company of to the you tone behind never knowing of field fame.</p>
</section>

<footer class="site-footer">
  <div class="foot-col foot-links" style="left:126px">
    <h4>Quick links</h4>
    <a>Home</a><a>Residential</a><a>Commercial</a><a>Portfolio</a><a>About</a><a>Contact Us</a>
  </div>
  <div class="foot-col" style="left:313px">
    <h4>Contact info</h4>
    <div class="contact-item"><svg width="12" height="10" viewBox="0 0 12 10"><path d="M0 0h12v10H0z M0 0l6 5 6-5" fill="none" stroke="var(--teal-2)" stroke-width="1.5"/></svg><span>Email:<br>info@example.com</span></div>
    <div class="contact-item"><svg width="12" height="12" viewBox="0 0 24 24"><path fill="var(--teal-2)" d="M6.6 10.8a15.1 15.1 0 0 0 6.6 6.6l2.2-2.2a1 1 0 0 1 1-.25 11.4 11.4 0 0 0 3.6.57 1 1 0 0 1 1 1V20a1 1 0 0 1-1 1A17 17 0 0 1 3 4a1 1 0 0 1 1-1h3.5a1 1 0 0 1 1 1c0 1.25.2 2.45.57 3.57a1 1 0 0 1-.25 1z"/></svg><span>Phone:<br>123-456-7890</span></div>
    <div class="contact-item"><svg width="12" height="14" viewBox="0 0 12 16"><path d="M6 0a6 6 0 0 0-6 6c0 4.5 6 10 6 10s6-5.5 6-10a6 6 0 0 0-6-6zm0 8.5A2.5 2.5 0 1 1 6 3.5a2.5 2.5 0 0 1 0 5z" fill="var(--teal-2)"/></svg><span>Location:<br>Some address line goes<br>here city name</span></div>
  </div>
  <div class="foot-col foot-news" style="left:562px">
    <h4>Newsletter</h4>
    <p>Join our mailing list to learn about our latest projects and product offerings</p>
    <div class="subscribe"><svg width="11" height="9" viewBox="0 0 12 10"><path d="M0 0h12v10H0z M0 0l6 5 6-5" fill="none" stroke="#aaa" stroke-width="1.5"/></svg>Enter your email...<svg class="send" width="16" height="16" viewBox="0 0 24 24"><path d="M2 12L22 3l-6 19-4-8z" fill="var(--teal-2)"/></svg></div>
  </div>
  <div class="foot-col" style="left:882px">
    <h4>Stay Connected</h4>
    <div class="socials"><span></span><span></span><span></span><span></span></div>
  </div>
  <span class="foot-rule"></span>
  <p class="copyright">©2023 Ashbrook Coating . All Rights Reserved. TERMS &amp; CONDITIONS</p>
  <span class="to-top"><svg width="14" height="14" viewBox="0 0 14 14"><path d="M7 12V2M2 7l5-5 5 5" fill="none" stroke="#fff" stroke-width="1.6"/></svg></span>
</footer>

<form class="quote-form">
  <div class="field f-name"><label>Name*</label><span></span></div>
  <div class="field f-email"><label>Email*</label><span></span></div>
  <div class="field f-phone"><label>Phone*</label><span></span></div>
  <div class="field f-address"><label>Address*</label><span></span></div>
  <div class="field f-city"><label>City*</label><span></span></div>
  <div class="field f-state"><label>State*</label><span></span></div>
  <div class="field f-message"><label>Message*</label><span></span></div>
  <div class="btn-submit">Submit Now</div>
</form>

</body>
</html>
```